Need a weekly post illustration to show bands that play.
Example next week
Februaray
Fri 2nd 10pm Peter Malvey

Sat 3rd 3pm Front Bar Stonewicker
5;30pm Front Bar Gareth Pilby
8pm Front baR Colm Burke
8pm Outback DJ Sandy
10;30 stage Lanterns Westward
Sunday 4th 6;30pm Stonewicker
I have attached pictures of front of our venue and outback area.
Also sample posters from other venues and our own.
I have also attached past posters and all logos
Please email me if you require anything further
Example next week
Februaray
Fri 2nd 10pm Peter Malvey

8pm Front baR Colm Burke
8pm Outback DJ Sandy

Target Market(s)

every age group

Industry/Entity Type

pub

Font styles to use
Serif

Colors
FFC000
F8CF3A
FAE287
FDF2CF
FEFAEE
EB3D1F
EC4F4E
F09395
F8D3D4
FCEDEE

Requirements
Must have
• Specific band time , name of band and area of venue
Nice to have
• Our brand is red , black and gold of logo. Would like to see this
Should not have
• Inaccurate information. Correct times and bands

```html
<!DOCTYPE html>
<html lang="en">
<head>
<meta charset="utf-8">
<title>Kinsella's Bar – Gig Guide</title>
<link rel="stylesheet" href="https://fonts.googleapis.com/css2?family=Cinzel:wght@700&family=Rye&family=Playfair+Display:wght@600&display=swap">
<style>
  :root {
    --canvas: #ffffff;
    --bar-dark: #2a1610;
    --bar-mid: #5a2a18;
    --bar-warm: #8a3b1c;
    --gold: #d9b25a;
    --gold-deep: #b8862a;
    --gig-gold: #b07a1a;
    --ink: #3a2a22;
    --pill: #3b2c25;
    --pill-text: #f3e6cf;
    --frame: #5f5f5f;
    --photo-a: #6b4a36;
    --photo-b: #3a2a22;
    --parch-light: #f2dcb4;
    --parch-edge: #c58a4d;
  }
  html, body { margin: 0; padding: 0; overflow: hidden; }
  body { width: 1200px; height: 1200px; background: var(--canvas); position: relative; }
  .poster {
    position: absolute; left: 152px; top: 39px; width: 896px; height: 1122px; overflow: hidden;
    background: linear-gradient(180deg, var(--bar-dark) 0%, var(--bar-mid) 30%, #3c2418 60%, var(--bar-warm) 100%);
  }
  .photo {
    position: absolute; border: 6px solid var(--frame);
    background: linear-gradient(135deg, var(--photo-a), var(--photo-b));
  }
  .venue-title {
    position: absolute; left: 0; width: 100%; text-align: center;
    font-family: 'Cinzel', serif; font-weight: 700; color: var(--gold); margin: 0;
  }
  .venue-title.name { top: 68px; font-size: 74px; letter-spacing: 1px; line-height: 1; }
  .venue-title.kind { top: 158px; font-size: 60px; line-height: 1; }
  .rule { position: absolute; top: 163px; height: 4px; background: var(--gold); }
  .parchment { position: absolute; left: 165px; top: 234px; }
  .gig-title {
    position: absolute; left: 0; width: 896px; top: 283px; text-align: center; margin: 0;
    font-family: 'Rye', serif; font-size: 62px; color: var(--gig-gold);
    -webkit-text-stroke: 1.5px var(--bar-dark);
  }
  .day {
    position: absolute; left: 286px; width: 327px; height: 40px; border-radius: 20px;
    background: var(--pill); color: var(--pill-text); text-align: center;
    font-family: 'Playfair Display', serif; font-weight: 600; font-size: 23px; line-height: 40px;
  }
  .slots { position: absolute; left: 275px; margin: 0; padding: 0; list-style: none;
    font-family: 'Playfair Display', serif; font-weight: 600; font-size: 22px; color: var(--ink); line-height: 32.5px; }
  .brand-seal {
    position: absolute; left: 649px; top: 867px; width: 224px; height: 224px; border-radius: 50%;
    background: var(--bar-dark); border: 8px solid var(--frame); box-sizing: border-box;
    display: flex; align-items: center; justify-content: center; text-align: center;
    font-family: 'Cinzel', serif; font-weight: 700; font-size: 28px; color: var(--gold); line-height: 1.1;
  }
</style>
</head>
<body>
<main class="poster">
  <div role="img" aria-label="Photo of the bar's outback area with signage" style="position:absolute;inset:0;background:radial-gradient(ellipse at 50% 15%, rgba(150,50,30,.55), transparent 60%);"></div>

  <div class="photo" role="img" aria-label="Photo of a soul band performing" style="left:-10px;top:170px;width:230px;height:175px;transform:rotate(-2deg);"></div>
  <div class="photo" role="img" aria-label="Photo of bar interior" style="left:-10px;top:350px;width:180px;height:150px;transform:rotate(-3deg);"></div>
  <div class="photo" role="img" aria-label="Photo of a musician on stage with audience" style="left:-10px;top:505px;width:190px;height:175px;transform:rotate(-3deg);"></div>
  <div class="photo" role="img" aria-label="Photo of a crowd at the venue" style="left:-10px;top:695px;width:190px;height:140px;transform:rotate(-2deg);"></div>
  <div class="photo" role="img" aria-label="Photo of a four-piece band" style="left:-10px;top:845px;width:200px;height:190px;transform:rotate(-3deg);"></div>
  <div class="photo" role="img" aria-label="Photo of a soul band performing" style="left:255px;top:1010px;width:340px;height:150px;transform:rotate(-3deg);"></div>
  <div class="photo" role="img" aria-label="Photo of a three-piece band" style="left:620px;top:180px;width:300px;height:205px;transform:rotate(-4deg);"></div>
  <div class="photo" role="img" aria-label="Photo of a musician on stage with audience" style="left:715px;top:480px;width:200px;height:170px;transform:rotate(-3deg);"></div>
  <div class="photo" role="img" aria-label="Photo of the bar's front exterior" style="left:720px;top:740px;width:200px;height:150px;transform:rotate(-3deg);"></div>

  <h1 class="venue-title name">KINSELLA'S</h1>
  <div class="rule" style="left:196px;width:150px;"></div>
  <div class="rule" style="left:559px;width:152px;"></div>
  <h2 class="venue-title kind">BAR</h2>

  <svg class="parchment" width="568" height="758" viewBox="0 0 568 758" aria-hidden="true">
    <defs>
      <radialGradient id="parch" cx="50%" cy="45%" r="65%">
        <stop offset="0%" stop-color="#f5e2c0"/>
        <stop offset="65%" stop-color="#e9c998"/>
        <stop offset="100%" stop-color="#c58a4d"/>
      </radialGradient>
    </defs>
    <path d="M30 12 L90 4 L150 14 L220 2 L300 10 L380 0 L460 12 L530 4 L556 40 L548 120 L562 210 L550 300 L566 400 L552 500 L564 600 L548 690 L520 742 L440 736 L360 752 L280 740 L200 756 L120 744 L40 752 L18 700 L26 600 L8 500 L22 400 L6 300 L20 200 L4 110 L18 50 Z" fill="url(#parch)"/>
  </svg>

  <h2 class="gig-title">GIG GUIDE</h2>

  <div class="day" style="top:402px;">Friday, February 2nd:</div>
  <ul class="slots" style="top:454px;">
    <li>10pm - Peter Malvey (Main Venue)</li>
  </ul>

  <div class="day" style="top:525px;">Saturday, February 3rd:</div>
  <ul class="slots" style="top:576px;">
    <li>3pm - Stonewicker (Front Bar)</li>
    <li>5:30pm - Gareth Pilby (Front Bar)</li>
    <li>8pm - Colm Burke (Front Bar)</li>
    <li>8pm - DJ Sandy (Outback)</li>
    <li>10:30pm - Lanterns Westward (Main Venue)</li>
  </ul>

  <div class="day" style="top:784px;">Sunday, February 4th:</div>
  <ul class="slots" style="top:835px;">
    <li>6:30pm - Stonewicker (Main Venue)</li>
  </ul>

  <div class="brand-seal">KINSELLA'S<br>BAR</div>
</main>
</body>
</html>
```